psd/html for a e wallet payment website designed

hi
i am in need of a psd / html for a whole website designed
the site is a e wallet /payment system i can i will provide a link to what type of style i am looking for but i can not stress this enough i do not want anyone replicating the website i am just providing the links to show you what kind of function and the content that is involved also, i have a srs with detailed pages you can read and refer to if need be
thanks of viewing
Vantoleaf.com
Brisklune.com
marblequivercoin.com
Qrdelivane.com

```html
<!DOCTYPE html>
<html lang="en">
<head>
<meta charset="utf-8">
<title>Corvane Pay</title>
<link rel="stylesheet" href="https://fonts.googleapis.com/css2?family=Arimo:wght@400;700&family=Oswald:wght@500&family=Open+Sans:wght@700&display=swap">
<style>
:root{
  --red:#e8141b;
  --red-dark:#c70d12;
  --ink:#3d3d3d;
  --muted:#555;
  --link:#1a8fc9;
  --page:#f1f2f3;
  --hero-band:#eceef0;
  --line:#c9c9c9;
  --footer:#1d1f22;
  --white:#fff;
}
*{box-sizing:border-box;margin:0;padding:0}
html,body{width:1177px;height:1200px;overflow:hidden}
body{position:relative;background:var(--page);font-family:"Arimo",Arial,sans-serif;color:var(--ink)}
.abs{position:absolute}
.top-strip{left:0;top:0;width:1177px;height:8px;background:var(--red)}
.header{left:0;top:8px;width:1177px;height:82px;background:var(--white);border-bottom:1px solid #d8d8d8}
.brand{left:196px;top:22px;display:flex;align-items:center;gap:10px}
.brand-mark{width:28px;height:28px;background:var(--red)}
.brand-name{font-weight:700;font-size:27px;color:var(--ink)}
.nav{left:582px;top:0;height:82px;display:flex}
.nav a{font-family:"Oswald",sans-serif;font-size:12px;color:#333;text-decoration:none;height:82px;display:flex;align-items:center;padding:0 17px}
.nav a.current{background:#e4e4e4;color:var(--red);border-bottom:3px solid var(--red);padding:0 11px}
.search{left:927px;top:0;width:53px;height:82px;border-left:1px solid #e2e2e2;border-right:1px solid #e2e2e2;display:flex;align-items:center;justify-content:center}
.hero-band{left:0;top:91px;width:1177px;height:331px;background:var(--hero-band)}
.slider{left:196px;top:102px;width:784px;height:292px;background:linear-gradient(90deg,#bcbcbc 0%,#9a9a9a 40%,#d8d8d8 70%,#6e6e6e 100%);box-shadow:0 14px 18px -10px rgba(0,0,0,.35)}
.slide-photo{left:420px;top:10px;width:300px;height:282px;background:linear-gradient(160deg,#8fa9a0,#c8476a 50%,#2a2a2a)}
.shop-btn{left:94px;top:96px;display:flex;height:55px}
.shop-btn .label{width:154px;background:var(--white);color:var(--red);font-family:"Open Sans",sans-serif;font-weight:700;font-size:24px;display:flex;align-items:center;justify-content:center}
.shop-btn .go{width:41px;background:#444;display:flex;align-items:center;justify-content:center}
.arrow-prev{left:14px;top:120px}
.arrow-next{left:750px;top:120px}
.dots{left:720px;top:275px;display:flex;gap:5px}
.dots span{width:10px;height:10px;border-radius:50%;background:var(--white);border:3px solid #1aa3dd}
.welcome{left:196px;top:440px;width:784px;text-align:center}
.welcome h1{font-weight:400;font-size:20px;color:var(--red)}
.welcome p{margin-top:14px;font-size:9.6px;line-height:19px;color:var(--muted)}
.feature{top:596px;width:260px;height:170px}
.feature .ring{left:0;top:0;width:60px;height:60px;border-radius:50%;border:4px solid #c8c8c8;background:var(--white);display:flex;align-items:center;justify-content:center}
.feature .icon{width:30px;height:26px;border-radius:4px}
.feature .stem{left:29px;top:60px;width:2px;height:110px;background:#bdbdbd}
.feature h2{left:82px;top:10px;font-weight:400;font-size:20px;color:var(--red);white-space:nowrap}
.feature p{left:80px;top:44px;font-size:9.6px;line-height:19px;color:var(--muted)}
.feature p span{display:block;white-space:nowrap}
.more{left:80px;top:130px;width:65px;height:30px;background:var(--red);color:var(--white);border-radius:5px;font-size:10px;display:flex;align-items:center;justify-content:center;box-shadow:0 2px 0 var(--red-dark)}
.divider{left:0;top:766px;width:1177px;height:1px;background:var(--line)}
.about{left:197px;top:804px;width:392px}
.about h2{font-weight:400;font-size:19px;color:var(--red)}
.about h3{font-weight:400;font-size:14px;color:var(--red);margin-top:8px}
.about h4{font-size:14px;color:#444;margin-top:18px}
.about p{font-size:9.6px;line-height:14px;letter-spacing:.5px;color:var(--muted);margin-top:4px}
.about a{color:var(--link);text-decoration:none}
.news{left:638px;top:804px;width:342px;height:290px}
.news h2{left:0;top:4px;font-weight:400;font-size:19px;color:var(--red)}
.news-ctrl{left:293px;top:0;display:flex;gap:3px}
.news-ctrl span{width:22px;height:19px;background:var(--white);border:1px solid #ccc;display:flex;align-items:center;justify-content:center}
.item{left:2px;width:340px;height:70px}
.item .thumb{left:0;top:0;width:99px;height:68px;border:2px solid var(--white);box-shadow:0 1px 3px rgba(0,0,0,.3)}
.item h5{left:120px;top:8px;font-size:11.2px;color:#222}
.item .by{left:120px;top:28px;font-size:9.6px;color:#222}
.item .by a{color:var(--link);text-decoration:none}
.item .date{left:120px;top:44px;font-size:9.6px;color:#222}
.footer-rule{left:0;top:1112px;width:1177px;height:6px;background:var(--red)}
.footer{left:0;top:1118px;width:1177px;height:82px;background:var(--footer)}
.foot-nav{left:395px;top:26px;display:flex;gap:0}
.foot-nav a{color:var(--white);font-size:10px;text-decoration:none;margin-right:41px}
.copy{left:554px;top:52px;color:var(--white);font-size:10px}
.social{left:900px;top:20px;display:flex;gap:7px}
.social span{width:22px;height:22px}
</style>
</head>
<body>
<div class="abs top-strip"></div>
<header class="abs header">
  <div class="abs brand"><span class="brand-mark"></span><span class="brand-name">Corvane Pay</span></div>
  <nav class="abs nav">
    <a class="current" href="#">Home</a><a href="#">About Us</a><a href="#">Services</a><a href="#">FAQ's</a><a href="#">Contact Us</a>
  </nav>
  <div class="abs search"><svg width="15" height="15" viewBox="0 0 15 15"><circle cx="6" cy="6" r="4.5" fill="none" stroke="#222" stroke-width="2"/><line x1="9.5" y1="9.5" x2="13.5" y2="13.5" stroke="#222" stroke-width="2"/></svg></div>
</header>

<div class="abs hero-band"></div>
<section class="abs slider" role="img" aria-label="Blurred city skyline behind a shopper holding bags and a card">
  <div class="abs slide-photo" role="img" aria-label="Shopper with colourful shopping bags"></div>
  <div class="abs shop-btn"><span class="label">Shop Now</span><span class="go"><svg width="12" height="16" viewBox="0 0 12 16"><polyline points="3,2 9,8 3,14" fill="none" stroke="#fff" stroke-width="2.5"/></svg></span></div>
  <svg class="abs arrow-prev" width="18" height="28" viewBox="0 0 18 28"><polyline points="14,3 4,14 14,25" fill="none" stroke="#1aa3dd" stroke-width="4"/></svg>
  <svg class="abs arrow-next" width="18" height="28" viewBox="0 0 18 28"><polyline points="4,3 14,14 4,25" fill="none" stroke="#e8141b" stroke-width="4"/></svg>
  <div class="abs dots"><span></span><span></span><span></span><span></span></div>
</section>

<section class="abs welcome">
  <h1>Welcome Corvane Pay</h1>
  <p>Lorem ipsum dolor sit amet, consectetur adipiscing elit. Nulla convallis egestas rhoncus. Donec facilisis fermentum sem, ac viverra ante luctus vel. Donec vel mauris quam. Aliquam pellentesque pellentesque turpis, ut bibendum sapien sollicitudin nec. Pellentesque posuere ornare placerat. Suspendisse potenti. Quisque massa tortor, tristique non tristique at, luctus sed massa. Donec libero eros, mollis ac...Lorem ipsum dolor sit amet, consectetur adipiscing elit. Nulla convallis egestas rhoncus. Donec facilisis fermentum sem, ac viverra ante luctus vel. Donec vel mauris quam.</p>
</section>

<article class="abs feature" style="left:197px">
  <div class="abs ring"><span class="icon" role="img" aria-label="Payment cards icon" style="background:#5aa6d6"></span></div>
  <div class="abs stem"></div>
  <h2 class="abs">Shoping Cards</h2>
  <p class="abs"><span>Lorem ipsum dolor sit amet, consectetur</span><span>adipiscing elit. Nulla convallis egestas rhon-</span><span>cus. Donec facilisis fermentum sem, ac</span><span>viverra ante luctus vel. Donec vel mauris</span></p>
  <a class="abs more">Read more..</a>
</article>
<article class="abs feature" style="left:466px">
  <div class="abs ring"><span class="icon" role="img" aria-label="Storefront icon" style="background:#c0573a"></span></div>
  <div class="abs stem"></div>
  <h2 class="abs">Stores</h2>
  <p class="abs"><span>Lorem ipsum dolor sit amet, consectetur</span><span>adipiscing elit. Nulla convallis egestas rhon-</span><span>cus. Donec facilisis fermentum sem, ac</span><span>viverra ante luctus vel. Donec vel mauris</span></p>
  <a class="abs more">Read more..</a>
</article>
<article class="abs feature" style="left:710px">
  <div class="abs ring"><span class="icon" role="img" aria-label="Stack of banknotes icon" style="background:#7c9a5a"></span></div>
  <div class="abs stem"></div>
  <h2 class="abs">Money</h2>
  <p class="abs"><span>Lorem ipsum dolor sit amet, consectetur</span><span>adipiscing elit. Nulla convallis egestas rhon-</span><span>cus. Donec facilisis fermentum sem, ac</span><span>viverra ante luctus vel. Donec vel mauris</span></p>
  <a class="abs more">Read more..</a>
</article>

<div class="abs divider"></div>

<section class="abs about">
  <h2>About Us</h2>
  <h3>Company</h3>
  <h4>Who we are?</h4>
  <p>Corvane Pay Inc is a company focusing on promoting mobile apps through a powerful and non incentivized discovery app channel. The company is based in London UK, established in 2013 with the help of the Cologne, Germany-based mobile media incubator, Halvren Ventures <a href="#">http://CorvanePay.com/</a></p>
  <h4 style="margin-top:26px">Who we are?</h4>
  <p>Corvane Inc believes that fast growing markets with great mobile marketing potential, are being underrated in terms of mobile acquisition. We believe that by introducing a powerful, transparent and affordable solution to mobile app developers, specially to small ones, growth opportunities have no limits. We are the friendly face of mobile acquisition for app developers.</p>
</section>

<section class="abs news">
  <h2 class="abs">News</h2>
  <div class="abs news-ctrl">
    <span><svg width="10" height="7" viewBox="0 0 10 7"><polyline points="1,6 5,2 9,6" fill="none" stroke="#999" stroke-width="2"/></svg></span>
    <span><svg width="10" height="7" viewBox="0 0 10 7"><polyline points="1,1 5,5 9,1" fill="none" stroke="#999" stroke-width="2"/></svg></span>
  </div>
  <div class="abs item" style="top:42px">
    <div class="abs thumb" role="img" aria-label="Hands reviewing printed documents" style="background:linear-gradient(135deg,#8a8f96,#c9ccd0)"></div>
    <h5 class="abs">Why You Need a Small Group</h5>
    <div class="abs by">by <a href="#">anselm</a></div>
    <div class="abs date">Oct 22, 2013</div>
  </div>
  <div class="abs item" style="top:130px">
    <div class="abs thumb" role="img" aria-label="Dark street art scene" style="background:linear-gradient(135deg,#3a4450,#8b8a6a)"></div>
    <h5 class="abs">Why You Need a Small Group</h5>
    <div class="abs by">by <a href="#">anselm</a></div>
    <div class="abs date">Oct 22, 2013</div>
  </div>
  <div class="abs item" style="top:218px">
    <div class="abs thumb" role="img" aria-label="Colourful app icons spilling from a phone" style="background:linear-gradient(135deg,#e8e8e8,#c06a6a 50%,#5a7fb0)"></div>
    <h5 class="abs">Why You Need a Small Group</h5>
    <div class="abs by">by <a href="#">anselm</a></div>
    <div class="abs date">Oct 22, 2013</div>
  </div>
</section>

<div class="abs footer-rule"></div>
<footer class="abs footer">
  <nav class="abs foot-nav"><a href="#">Home</a><a href="#">About Us</a><a href="#">Apps</a><a href="#">Jobs</a><a href="#">News</a><a href="#">Contact Us</a></nav>
  <div class="abs copy">@ Corvane Pay 2014</div>
  <div class="abs social">
    <span role="img" aria-label="Social link" style="background:#3b5b9a"></span>
    <span role="img" aria-label="Social link" style="background:#1ba0e2"></span>
    <span role="img" aria-label="Social link" style="background:#c8232c"></span>
  </div>
</footer>
</body>
</html>
```